Business card - Kestrel Bay Framing

Design a business card utilizing the given logo.
colors we like: Black, greys, Teal, blues.
Tri color card, horizontal orientation likely
Logo and name likely best on top.
Info on card:

Dennis Harcourt
#5 - 1845 Larchmont Way
Surrey, B.C. V7T 3K2

604.555.0193
dennisharcourt@telvane.ca

Slogan: "Building Dreams"

We are a construction company that specializes in new home construction on the West coast of BC Canada. Bay Framing designs of high end homes.

```html
<!DOCTYPE html>
<html lang="en">
<head>
<meta charset="utf-8">
<title>Kestrel Bay Framing – Business Card</title>
<link href="https://fonts.googleapis.com/css2?family=Roboto:wght@400;500&family=Roboto+Condensed:wght@700&display=swap" rel="stylesheet">
<style>
  :root {
    --backdrop: #2b2b2d;
    --card: #232325;
    --card-edge: #1b1b1d;
    --teal: #1fbfd0;
    --teal-deep: #14939f;
    --teal-faint: #3b5558;
    --ink-dark: #1a1a1a;
    --text-light: #f2f2f2;
    --text-grey: #b9b9bb;
  }
  * { box-sizing: border-box; margin: 0; padding: 0; }
  html, body {
    width: 1200px; height: 1000px; overflow: hidden;
    background: var(--backdrop);
  }
  .stage {
    width: 1200px; height: 1000px;
    display: flex; align-items: center; justify-content: center;
  }
  .card {
    position: relative;
    width: 1000px; height: 572px;
    background: var(--card);
    overflow: hidden;
    box-shadow: 0 18px 40px rgba(0,0,0,.45);
    font-family: "Roboto", Arial, sans-serif;
  }
  .slogan-band {
    position: absolute; left: 0; top: 0; bottom: 0;
    width: 62px;
    background: var(--teal);
    display: flex; align-items: center; justify-content: center;
  }
  .slogan {
    transform: rotate(-90deg);
    white-space: nowrap;
    font-family: "Roboto Condensed", "Arial Narrow", sans-serif;
    font-weight: 700;
    font-size: 28px;
    letter-spacing: 3px;
    color: var(--ink-dark);
  }
  .decor-mark {
    position: absolute; right: -120px; bottom: 40px;
  }
  .brand {
    position: absolute; left: 112px; top: 62px;
    display: flex; align-items: center; gap: 26px;
  }
  .brand-dot {
    width: 118px; height: 118px; border-radius: 50%;
    background: var(--teal-deep);
    flex: none;
  }
  .brand-name {
    font-weight: 400;
    font-size: 62px;
    letter-spacing: 4px;
    text-transform: uppercase;
    color: var(--teal);
    line-height: 1;
  }
  .contact {
    position: absolute; left: 112px; top: 318px;
  }
  .person {
    font-weight: 400;
    font-size: 34px;
    letter-spacing: 3px;
    text-transform: uppercase;
    color: var(--teal);
    margin-bottom: 28px;
  }
  .line {
    font-size: 22px;
    color: var(--text-light);
    line-height: 32px;
    letter-spacing: .5px;
  }
  .line .label { color: var(--teal); margin-right: 10px; }
  .address { margin-top: 20px; }
  .address .line:last-child { color: var(--text-grey); }
</style>
</head>
<body>
<main class="stage">
  <article class="card">
    <div class="slogan-band"><span class="slogan">BUILDING DREAMS</span></div>

    <svg class="decor-mark" width="320" height="320" viewBox="0 0 320 320" aria-hidden="true">
      <circle cx="160" cy="160" r="160" fill="var(--teal-faint)"/>
    </svg>

    <header class="brand">
      <span class="brand-dot"></span>
      <h1 class="brand-name">Kestrel Bay Framing</h1>
    </header>

    <section class="contact">
      <h2 class="person">Dennis Harcourt</h2>
      <p class="line"><span class="label">P:</span>604.555.0193</p>
      <p class="line"><span class="label">E:</span>dennisharcourt@telvane.ca</p>
      <div class="address">
        <p class="line">#5 - 1845 Larchmont Way</p>
        <p class="line">Surrey, B.C. V7T 3K2</p>
      </div>
    </section>
  </article>
</main>
</body>
</html>
```